business card design for a small scale specialty cut flower farm

We need a business card design for Hollowmere Bloom Farm based in Langley, BC, Canada. We produce specialty, high-end cut flowers and sell locally to florists, local shops and markets and the end user through bouquet subscriptions. The final business card design should be memorable and have a timeless or vintage feel. We would prefer a square shape.
Updates

Target Market(s)

florists, shops and seasonal markets, local flower lovers

Industry/Entity Type

Floral

Contact Information for Business Card

Tamsin Ellery Voss, Grower
Langley, BC, Canada
website: hollowmerebloomfarm.example
instagram: @hollowmerebloomfarm
Tel: 555.317.4290
facebook: www.facebook.example/hollowmereblooms/

Font styles to use
Serif
Decorative
Script

Requirements
Must have
• soft black background colour on front side, the included logo and catch phrase: Fresh Local Seasonal
Nice to have
• phone number and website address on front of card, included photo 6539 incorporated onto the back, possibly photo 6609 as well.

```html
<!DOCTYPE html>
<html lang="en">
<head>
<meta charset="utf-8">
<title>Tamsin Ellery Voss – Business Card</title>
<link rel="stylesheet" href="https://fonts.googleapis.com/css2?family=Great+Vibes&family=Roboto:wght@300;400&display=swap">
<style>
  :root {
    --forest: #2d4a2b;
    --ink: #222222;
    --paper: #ffffff;
  }
  * { margin: 0; padding: 0; box-sizing: border-box; }
  html, body {
    width: 1200px;
    height: 749px;
    overflow: hidden;
    background: var(--paper);
  }
  .card {
    position: relative;
    width: 1200px;
    height: 749px;
    background: var(--paper);
    font-family: "Roboto", Arial, sans-serif;
    font-weight: 300;
    color: var(--ink);
  }
  .identity {
    position: absolute;
    left: 115px;
    top: 109px;
    height: 95px;
    padding-left: 25px;
    border-left: 13px solid var(--forest);
  }
  .identity__name {
    font-family: "Great Vibes", cursive;
    font-weight: 400;
    font-size: 56px;
    line-height: 1;
    letter-spacing: 1px;
    color: var(--forest);
    margin-top: 6px;
    margin-left: -13px;
    white-space: nowrap;
  }
  .identity__role {
    font-size: 32px;
    line-height: 1;
    margin-top: 0;
    margin-left: -13px;
  }
  .contact-line {
    position: absolute;
    left: 115px;
    display: flex;
    align-items: center;
    font-size: 29px;
    white-space: nowrap;
  }
  .contact-line--web { top: 466px; }
  .contact-line--phone { top: 520px; }
  .contact-line__icon { fill: var(--forest); margin-right: 6px; }
  .contact-line--web .contact-line__icon { margin-left: 2px; margin-right: 14px; }
  .divider {
    position: absolute;
    left: 116px;
    top: 580px;
    width: 969px;
    height: 5px;
    background: var(--forest);
  }
  .social {
    position: absolute;
    top: 602px;
    display: flex;
    align-items: center;
    font-size: 24.5px;
    white-space: nowrap;
  }
  .social--page { left: 117px; }
  .social--handle { right: 116px; }
  .social__dot {
    width: 43px;
    height: 43px;
    border-radius: 50%;
    background: var(--forest);
    flex: none;
  }
  .social--page .social__dot { margin-right: 12px; }
  .social--handle .social__dot { margin-right: 5px; }
</style>
</head>
<body>
  <main class="card">
    <header class="identity">
      <h1 class="identity__name">Tamsin Ellery Voss</h1>
      <p class="identity__role">Owner</p>
    </header>

    <div class="contact-line contact-line--web">
      <svg class="contact-line__icon" width="34" height="34" viewBox="0 0 34 34" aria-hidden="true">
        <circle cx="17" cy="17" r="16" fill="var(--forest)"/>
        <g fill="none" stroke="#fff" stroke-width="2">
          <ellipse cx="17" cy="17" rx="7" ry="16"/>
          <line x1="17" y1="1" x2="17" y2="33"/>
          <line x1="1" y1="17" x2="33" y2="17"/>
          <path d="M4 9 H30 M4 25 H30"/>
        </g>
      </svg>
      <span>www.hollowmerebloomfarm.example</span>
    </div>

    <div class="contact-line contact-line--phone">
      <svg class="contact-line__icon" width="44" height="34" viewBox="0 0 44 34" aria-hidden="true">
        <path d="M2 10 C2 3 10 1 22 1 C34 1 42 3 42 10 L42 13 L32 13 L32 8 C28 7 16 7 12 8 L12 13 L2 13 Z"/>
        <path d="M14 11 L30 11 L38 24 L38 33 L6 33 L6 24 Z"/>
        <circle cx="22" cy="23" r="5" fill="#fff"/>
        <circle cx="22" cy="23" r="2.5"/>
      </svg>
      <span>(555) 317-4290</span>
    </div>

    <div class="divider" role="presentation"></div>

    <div class="social social--page">
      <span class="social__dot" aria-hidden="true"></span>
      <span>www.pagenest.example/hollowmereblooms</span>
    </div>

    <div class="social social--handle">
      <span class="social__dot" aria-hidden="true"></span>
      <span>@hollowmerebloomfarm</span>
    </div>
  </main>
</body>
</html>
```